Brightmoor Law Letterhead for Law firm must be modern and use the logo I uploaded.

Hello I want a clean modern professional letterhead for my law firm Brightmoor Law. A logo has already been created and all files have been uploaded. The information for the firm can be given through message. Please use the logo that has already been created. Please also use the color scheme of that logo. (blue and white).

Target Market(s)

General Public

Industry/Entity Type

Law Firm

Colors

Designer to choose colors to be used in the design.

Requirements
Must have
• This must be a modern professional letterhead
Nice to have
• My logo that is included in file form
Should not have
• Should not have logo that is not the one I uploaded.

```html
<!DOCTYPE html>
<html lang="en">
<head>
<meta charset="utf-8">
<title>Brightmoor Law Letterhead</title>
<link href="https://fonts.googleapis.com/css2?family=Lato:wght@400;700&family=Dancing+Script:wght@500&display=swap" rel="stylesheet">
<style>
  :root {
    --ink: #141414;
    --navy: #2b2f6b;
    --paper: #ffffff;
    --backdrop: #e9e9ea;
    --text: #1d1d1d;
  }
  * { margin: 0; padding: 0; box-sizing: border-box; }
  html, body {
    width: 1200px; height: 960px; overflow: hidden;
    background: var(--backdrop);
    font-family: "Lato", Arial, sans-serif;
    color: var(--text);
  }
  .letterhead {
    position: absolute; left: 282px; top: 30px;
    width: 636px; height: 900px;
    background: var(--paper);
    box-shadow: 0 2px 10px rgba(0,0,0,0.12);
    overflow: hidden;
  }
  .header-wave { position: absolute; left: 0; top: 0; width: 636px; height: 160px; }
  .brand {
    position: absolute; left: 36px; top: 28px; width: 200px;
    display: flex; flex-direction: column; align-items: center; gap: 14px;
  }
  .brand-mark {
    width: 38px; height: 38px;
    border: 2px solid var(--paper);
  }
  .firm-name {
    color: var(--paper);
    font-size: 12px; font-weight: 400;
    letter-spacing: 6px; text-transform: uppercase;
    white-space: nowrap;
  }
  .contact {
    position: absolute; left: 494px; top: 72px;
    font-style: normal;
    font-size: 8.5px; line-height: 11px; color: var(--text);
  }
  .contact .address { margin-bottom: 4px; }
  .contact-row { display: flex; align-items: center; gap: 4px; }
  .contact-row svg { width: 7px; height: 7px; fill: var(--navy); flex: none; }
  .letter-body {
    position: absolute; left: 72px; top: 196px; width: 490px;
    font-size: 10.5px; line-height: 13.5px;
  }
  .date { margin-bottom: 16px; font-size: 12px; }
  .recipient { margin-bottom: 12px; font-size: 12px; line-height: 14px; }
  .salutation { font-weight: 700; font-size: 15px; margin: 16px 0 12px; }
  .letter-body p.para { margin-bottom: 13px; }
  .closing { margin-top: 24px; font-size: 11.5px; }
  .signature {
    margin-top: 44px; margin-left: 80px;
    font-family: "Dancing Script", cursive;
    font-size: 32px; color: var(--ink);
  }
</style>
</head>
<body>
  <main class="letterhead">
    <svg class="header-wave" viewBox="0 0 636 160" aria-hidden="true">
      <path d="M0,0 H636 V18 C570,20 520,28 460,46 C380,72 330,110 230,120 C150,128 60,128 0,128 Z" fill="var(--ink)"/>
      <path d="M150,135 C260,127 330,104 410,68" fill="none" stroke="var(--navy)" stroke-width="2.5"/>
      <path d="M0,143 C80,143 170,141 250,133 C360,121 410,84 480,58 C540,38 590,32 636,30" fill="none" stroke="var(--navy)" stroke-width="7"/>
    </svg>
    <div class="brand">
      <div class="brand-mark"></div>
      <div class="firm-name">Brightmoor Law</div>
    </div>

    <address class="contact">
      <div class="address">Your address, City<br>State, Zip 1234</div>
      <div class="contact-row"><svg viewBox="0 0 10 10"><path d="M2 1 L4 1 L5 3 L4 4 Q5 6 6 6 L7 5 L9 6 L9 8 Q8 9 7 9 Q1 8 1 2 Q1 1 2 1Z"/></svg>123 456 789</div>
      <div class="contact-row"><svg viewBox="0 0 10 10"><path d="M1 2 H9 V8 H1 Z"/></svg>info@brightmoorlaw.com</div>
      <div class="contact-row"><svg viewBox="0 0 10 10"><circle cx="5" cy="5" r="4"/></svg>www.brightmoorlaw.com</div>
    </address>

    <section class="letter-body">
      <p class="date">January-03-2020</p>
      <p class="recipient">Mr. Peter Hale<br>President</p>
      <p class="recipient">Kestrel Corporation<br>123 Street Name, Suite# 10<br>City, State, 120023</p>
      <p class="salutation">Dear Mr. Hale</p>
      <p class="para">Lorem ipsum dolor sit amet, consectetur adipiscing elit, sed do eiusmod tempor incididunt ut labore et dolore magna aliqua. Ut enim ad minim veniam, quis nostrud exercitation ullamco laboris nisi ut aliquip ex ea commodo consequat. Duis aute irure dolor in reprehenderit in voluptate velit esse cillum dolore eu fugiat nulla pariatur.</p>
      <p class="para">Lorem ipsum dolor sit amet, consectetur adipiscing elit, sed do eiusmod tempor incididunt ut labore et dolore magna aliqua. Ut enim ad minim veniam, quis nostrud exercitation ullamco laboris nisi ut aliquip ex ea commodo consequat. Duis aute irure dolor in reprehenderit in voluptate velit esse cillum dolore eu fugiat nulla pariatur.</p>
      <p class="para">Lorem ipsum dolor sit amet, consectetur adipiscing elit, sed do eiusmod tempor incididunt ut labore et dolore magna aliqua. Ut enim ad minim veniam, quis nostrud exercitation ullamco laboris nisi ut aliquip ex ea commodo consequat.</p>
      <p class="para">Excepteur sint occaecat cupidatat non proident, sunt in culpa qui officia deserunt mollit anim id est laborum. re et dolore magnam aliquam quaerat voluptatem.</p>
      <p class="closing">Regards</p>
      <p class="signature">Daniel Price</p>
    </section>
  </main>
</body>
</html>
```